Webdesign for blog, vlog and website
The designs for my website were better than what I expected when I started this contest. I knew I needed a call-to-action on my homepage, but I thought it wouldn't be possible and I didn't ask for it either. But Anselmo did it anyway. Furthermore, his design looked very good. For that reason I selected him as winner already before I should. I am very happy.

```html
<!DOCTYPE html>
<html lang="nl">
<head>
<meta charset="utf-8">
<title>Vondrel – Webshop &amp; Blog</title>
<link rel="stylesheet" href="https://fonts.googleapis.com/css2?family=Montserrat:wght@400;500&family=Open+Sans:ital,wght@0,400;0,600;0,700;1,400&display=swap">
<style>
  :root{
    --blue:#1212ee;
    --blue-deep:#0b0bc8;
    --bar:#4a4ad0;
    --ink:#333;
    --muted:#777;
    --page:#ffffff;
    --canvas:#e9eaef;
    --frame:#3a3a3e;
  }
  *{box-sizing:border-box;margin:0;padding:0}
  html,body{width:1200px;height:800px;overflow:hidden}
  body{background:var(--canvas);font-family:"Open Sans",sans-serif;color:var(--ink);position:relative}

  /* ---------- Desktop webshop page ---------- */
  .shop-page{position:absolute;left:20px;top:20px;width:620px;height:760px;background:var(--page);overflow:hidden;box-shadow:0 2px 10px rgba(0,0,0,.08)}
  .blog-strip{display:flex;height:170px}
  .blog-photo-dark{width:210px;height:100%;background:linear-gradient(160deg,#111 40%,#3a3430);position:relative}
  .date-badge-small{position:absolute;right:0;top:0;width:70px;height:56px;background:var(--blue);color:#fff;font-size:34px;font-weight:300;display:flex;align-items:center;justify-content:center;font-family:"Open Sans",sans-serif}
  .date-badge-small::after{content:"";position:absolute;right:-8px;top:14px;border:8px solid transparent;border-left-color:var(--blue);border-right:0}
  .blog-excerpt{width:200px;padding:18px 16px;font-size:11px;font-style:italic;color:var(--muted);line-height:1.5}
  .blog-excerpt p{margin-bottom:12px}
  .read-more{display:flex;align-items:center;gap:6px;color:var(--blue);font-style:normal;font-size:11px;text-transform:uppercase}
  .blog-photo-light{flex:1;background:linear-gradient(120deg,#e8e4e0,#d8b89a 45%,#f0eeee 70%,#e6c0b0)}

  .shop-heading{text-align:center;margin-top:34px}
  .shop-heading h2{font-family:"Montserrat",sans-serif;font-weight:400;font-size:40px;color:var(--blue);letter-spacing:-.5px}
  .shop-heading .tagline{font-family:"Montserrat",sans-serif;font-size:15px;letter-spacing:4px;color:var(--blue);margin-top:2px}
  .shop-heading svg{display:block;margin:6px auto 0}

  .product-grid{display:grid;grid-template-columns:repeat(4,1fr);gap:18px;padding:30px 24px 0}
  .product{text-align:center}
  .product-image{height:120px;border-radius:4px;margin-bottom:18px}
  .img-cow{background:radial-gradient(circle,#6b5444 30%,#ffffff 72%)}
  .img-cowboy{background:radial-gradient(ellipse 40% 50%,#5a4a3e 40%,#fff 80%)}
  .img-mat{background:radial-gradient(ellipse 50% 45%,#b98a4f 45%,#fff 85%)}
  .img-stamp{background:radial-gradient(circle,#d9b27c 35%,#fff 75%)}
  .product h3{font-size:12.5px;font-weight:600;color:#555;margin-bottom:6px}
  .product p{font-size:10px;font-style:italic;color:#555;line-height:1.75;padding-bottom:8px;border-bottom:2px dotted #999}
  .price{font-size:22px;color:var(--blue);margin-top:10px;letter-spacing:-.5px}
  .vat{font-size:8.5px;color:#555;font-style:italic}

  /* ---------- Tablet blog page ---------- */
  .blog-page{position:absolute;left:660px;top:20px;width:520px;height:760px;background:var(--page);border:5px solid var(--frame);overflow:hidden}
  .site-header{height:58px;border-top:3px solid var(--blue);display:flex;align-items:center;justify-content:space-between;padding:0 18px}
  .brand{display:flex;align-items:center;gap:6px}
  .brand-dot{width:14px;height:14px;border-radius:50%;background:var(--blue)}
  .brand-name{font-size:19px;font-weight:600;color:var(--blue)}
  .menu-icon{display:flex;flex-direction:column;gap:3px}
  .menu-icon span{display:block;width:20px;height:2px;background:var(--blue)}
  .header-bar{height:7px;background:var(--bar)}
  .filter-row{display:flex;justify-content:space-between;align-items:center;padding:0 18px;height:42px;font-size:10px;text-transform:uppercase}
  .filter-row .entries{display:flex;gap:16px;color:#444}
  .filter-row .entries .active{color:var(--blue);font-weight:600}
  .filter-row .sep{color:#aaa}
  .filter-row .cats{display:flex;gap:10px;color:var(--blue);font-weight:600}
  .video{position:relative;margin:0 18px;height:410px;background:linear-gradient(180deg,#2fa1e0,#1f90d8 60%,#3aa6b0);}
  .video .play{position:absolute;left:50%;top:52%;transform:translate(-50%,-50%)}
  .article{display:flex;gap:18px;padding:16px 22px 0}
  .date-badge{flex:none;width:64px;height:86px;background:var(--blue);color:#fff;text-align:center;position:relative}
  .date-badge .month{font-size:9.5px;text-transform:uppercase;padding:8px 0 4px;border-bottom:1px dashed rgba(255,255,255,.8);margin:0 6px}
  .date-badge .day{font-size:36px;font-weight:300;line-height:54px}
  .date-badge::after{content:"";position:absolute;right:-7px;top:44px;border:7px solid transparent;border-left-color:var(--blue);border-right:0}
  .article h1{font-size:12.5px;font-weight:700;color:var(--blue);text-transform:uppercase;line-height:1.35;margin-bottom:14px}
  .article p{font-size:10px;color:var(--muted);line-height:1.6;margin-bottom:12px;text-align:justify}
</style>
</head>
<body>

<section class="shop-page">
  <div class="blog-strip">
    <div class="blog-photo-dark" role="img" aria-label="Photo of a hand holding a spray bottle on a dark background">
      <div class="date-badge-small">06</div>
    </div>
    <div class="blog-excerpt">
      <p>Lorem ipsum dolor sit amet, consectetur adipiscing elit, sed do eiusmod tempor incididunt ut labore et dolore magna aliqua.</p>
      <p>Lorem ipsum dolor sit amet, consectetur adipiscing elit, sed do eiusmod tempor incididunt ut labore et dolore magna</p>
      <span class="read-more">
        <svg width="12" height="12" viewBox="0 0 12 12"><circle cx="6" cy="6" r="5.3" fill="none" stroke="#777" stroke-width="1"/><path d="M4 6h4M6.3 4l2 2-2 2" fill="none" stroke="#777" stroke-width="1"/></svg>
        Read more
      </span>
    </div>
    <div class="blog-photo-light" role="img" aria-label="Photo of a woman with long hair reaching out her hand"></div>
  </div>

  <header class="shop-heading">
    <h2>From My Webshop</h2>
    <div class="tagline">NICE PRODUCTS... BEST PRICE</div>
    <svg width="280" height="22" viewBox="0 0 280 22"><path d="M4 20 Q120 -2 276 12 L275 17 Q130 6 6 21 Z" fill="#1212ee"/></svg>
  </header>

  <div class="product-grid">
    <article class="product">
      <div class="product-image img-cow" role="img" aria-label="Cast iron welcome sign with a cow head and stars"></div>
      <h3>Welkom bord Ranch koe</h3>
      <p>Lorem ipsum dolor sit amet, consectetur adipiscing elit, sed do eiusmod tempor incididunt ut labore et dolore magna aliqua.</p>
      <div class="price">€ 14,99</div>
      <div class="vat">inkl. 19% MwSt.</div>
    </article>
    <article class="product">
      <div class="product-image img-cowboy" role="img" aria-label="Cast iron welcome sign with a cowboy figure"></div>
      <h3>Welkom bord Ranch cowboy</h3>
      <p>Lorem ipsum dolor sit amet, consectetur adipiscing elit, sed do eiusmod tempor incididunt ut labore et dolore magna aliqua.</p>
      <div class="price">€ 14,99</div>
      <div class="vat">inkl. 19% MwSt.</div>
    </article>
    <article class="product">
      <div class="product-image img-mat" role="img" aria-label="Coir doormat with a two-sided message"></div>
      <h3>Deurmat dubbele boodschap</h3>
      <p>Lorem ipsum dolor sit amet, consectetur adipiscing elit, sed do eiusmod tempor incididunt ut labore et dolore magna aliqua.</p>
      <div class="price">€ 14,99</div>
      <div class="vat">inkl. 19% MwSt.</div>
    </article>
    <article class="product">
      <div class="product-image img-stamp" role="img" aria-label="Wooden stamp with a red base"></div>
      <h3>Stempel hout rood</h3>
      <p>Lorem ipsum dolor sit amet, consectetur adipiscing elit, sed do eiusmod tempor incididunt ut labore et dolore magna aliqua.</p>
      <div class="price">€ 14,99</div>
      <div class="vat">inkl. 19% MwSt.</div>
    </article>
  </div>
</section>

<section class="blog-page">
  <header class="site-header">
    <div class="brand"><span class="brand-dot"></span><span class="brand-name">Vondrel</span></div>
    <div class="menu-icon" aria-label="Menu"><span></span><span></span><span></span></div>
  </header>
  <div class="header-bar"></div>

  <nav class="filter-row">
    <div class="entries">
      <span class="active">10 entries</span><span class="sep">|</span>
      <span>20 entries</span><span class="sep">|</span>
      <span>30 entries</span>
    </div>
    <div class="cats"><span>All ideas ⌄</span><span class="sep">|</span><span>Blog &amp; vlogs ⌄</span></div>
  </nav>

  <div class="video" role="img" aria-label="Vlog video still of a smiling woman in a green top against a blue wall">
    <svg class="play" width="124" height="124" viewBox="0 0 124 124">
      <path d="M62 4 A58 58 0 1 0 120 62" fill="none" stroke="#fff" stroke-width="5"/>
      <path d="M80 9 A58 58 0 0 1 115 40" fill="none" stroke="#fff" stroke-width="5"/>
      <path d="M47 38 L88 62 L47 86 Z" fill="none" stroke="#fff" stroke-width="5" stroke-linejoin="round"/>
    </svg>
  </div>

  <article class="article">
    <div class="date-badge"><div class="month">April</div><div class="day">02</div></div>
    <div>
      <h1>Lorem ipsum dolor sit amet, consectetur adipiscing elitlorem ipsum dolor sit amet, consectetur adipiscing elit</h1>
      <p>Lorem ipsum dolor sit amet, consectetur adipiscing elit, sed do eiusmod tempor incididunt ut labore et dolore magna aliqua.</p>
      <p>Lorem ipsum dolor sit amet, consectetur adipiscing elit, sed do eiusmod tempor incididunt ut labore et dolore magna aliqua. Lorem ipsum dolor sit amet, consectetur adipiscing elit, sed do eiusmod tempor incididunt ut labore et dolore magna aliqua. Lorem ipsum dolor sit amet, consectetur adipiscing elit, sed do eiusmod tempor incididunt ut labore et dolore magna</p>
    </div>
  </article>
</section>

</body>
</html>
```